BRINDLE GULL WATERS is a underwater remotely controlled vehicle company

Need a website that explains what we do, how to reach, and prices.

Target Market(s)

Mariners of all sorts

Industry/Entity Type

Boat and marine

Coding

Coded - Design and coding required

Number of Pages Required

3 page

Font styles to use
Serif
Sans Serif

Colors
0054AA
0677BA
7BADD7
CADEEF
E8F1F8
00AB8E
00BBA5
67D7C9
C6EFE9
E9F9F6
FFF300
FFF600
FEFA6F
FFFEC7
FFFEE8

Requirements
Must have
• Videos, photos, contact info. What we do. Where we are.

```html
<!DOCTYPE html>
<html lang="en">
<head>
<meta charset="utf-8">
<title>Brindle Gull Waters — Underwater ROV</title>
<link rel="stylesheet" href="https://fonts.googleapis.com/css2?family=Red+Hat+Display:wght@400;500;600;700&display=swap">
<style>
:root{
  --navy:#0b2a5c;
  --deep:#123a66;
  --sea:#1c4a6e;
  --accent:#fa5a32;
  --ink:#1b1b1b;
  --text:#4a4a4a;
  --muted:#8a8a8a;
  --line:#d9d9d9;
  --soft:#f4f4f4;
  --white:#ffffff;
  --backdrop:#f7f7f7;
}
*{box-sizing:border-box;margin:0;padding:0}
html,body{width:1200px;height:4313px;overflow:hidden}
body{background:var(--backdrop);font-family:"Red Hat Display",Arial,sans-serif;color:var(--ink)}
.page{position:absolute;left:127px;top:64px;width:946px;height:4177px;background:var(--white);overflow:hidden}
.abs{position:absolute}

/* nav */
.nav{position:absolute;left:0;top:0;width:946px;height:45px;background:var(--white)}
.brand{position:absolute;left:96px;top:9px;display:flex;align-items:center;gap:6px;font-size:10px;font-weight:600;color:var(--navy)}
.brand-dot{width:26px;height:26px;border-radius:50%;background:var(--deep)}
.nav-link{position:absolute;top:15px;font-size:11.5px;color:var(--ink)}
.nav-link.active{color:var(--accent);text-decoration:underline}
.nav-divider{position:absolute;left:792px;top:13px;width:1px;height:18px;background:var(--line)}
.cart-badge{position:absolute;left:847px;top:10px;width:12px;height:12px;border-radius:50%;background:var(--ink);color:#fff;font-size:8px;text-align:center;line-height:12px}

/* hero */
.hero{position:absolute;left:0;top:45px;width:946px;height:475px;background:linear-gradient(180deg,#0d2f5e 0%,#0b3a6e 55%,#0a2c58 100%)}
.hero-curve{position:absolute;left:0;top:45px}
.hero-title{position:absolute;left:0;top:155px;width:946px;text-align:center;color:#fff;font-size:28px;font-weight:500;line-height:34px}
.hero-sub{position:absolute;left:0;top:224px;width:946px;text-align:center;color:#fff;font-size:13px}
.btn-white{position:absolute;left:406px;top:283px;width:134px;height:37px;border-radius:19px;background:#fff;color:var(--ink);font-size:13px;font-weight:600;text-align:center;line-height:37px}
.rov{border-radius:46% 46% 50% 50%/40% 40% 60% 60%;background:radial-gradient(ellipse at 50% 35%,#8a8d92 0%,#4b4e53 55%,#26282b 100%)}
.hero-rov{position:absolute;left:312px;top:399px;width:318px;height:180px}

/* intro */
.photo-dive{position:absolute;left:82px;top:768px;width:256px;height:279px;background:linear-gradient(160deg,#1c5aa8 0%,#0f3e86 50%,#0b2b60 100%)}
.photo-fish{position:absolute;left:217px;top:939px;width:184px;height:138px;border:6px solid #fff;background:linear-gradient(135deg,#3cb6e8 0%,#1c9fd9 60%,#7c4a2b 100%)}
.h2{font-size:26px;font-weight:500;line-height:30px;color:var(--ink)}
.intro-title{position:absolute;left:495px;top:761px;width:390px}
.intro-copy{position:absolute;left:495px;top:838px;width:372px;font-size:11.5px;line-height:19.4px;color:var(--text)}
.btn-accent{position:absolute;height:37px;border-radius:19px;background:var(--accent);color:#fff;font-size:13px;font-weight:600;text-align:center;line-height:37px}

/* video band */
.video-band{position:absolute;left:0;top:1201px;width:946px;height:414px;background:linear-gradient(180deg,#173f6a 0%,#1d4b6c 50%,#163c5c 100%)}
.video-title{position:absolute;left:82px;top:1365px;font-size:30px;font-weight:400;color:#fff}
.video-copy{position:absolute;left:82px;top:1409px;width:240px;font-size:11.5px;line-height:21px;color:#dfe8f0}
.play{position:absolute;left:441px;top:1378px}

/* line-up */
.lineup-title{position:absolute;left:0;top:1693px;width:946px;text-align:center;font-size:28px;font-weight:400}
.tabs{position:absolute;left:204px;top:1766px;width:538px;height:26px;border-bottom:1px solid var(--line)}
.tab{position:absolute;top:0;font-size:12.5px;color:var(--ink)}
.tab-underline{position:absolute;left:204px;top:1790px;width:114px;height:3px;background:var(--accent)}
.lineup-rov{position:absolute;left:82px;top:1866px;width:271px;height:159px}
.lineup-name{position:absolute;left:466px;top:1915px;font-size:20px;font-weight:500}
.lineup-copy{position:absolute;left:466px;top:1950px;width:400px;font-size:12px;line-height:24px;color:var(--text)}

/* features */
.features-title{position:absolute;left:82px;top:2084px;font-size:24px;font-weight:500}
.feature{position:absolute;height:26px;border-bottom:1px solid var(--line);font-size:11.5px;line-height:16px;color:var(--ink)}
.feature.left{left:82px;width:451px}
.feature.right{left:565px;width:297px}
.feature.last{border-bottom:none}

/* product */
.product{position:absolute;left:0;top:2606px;width:946px;height:418px;background:var(--soft)}
.product-title{position:absolute;left:85px;top:2693px;font-size:26px;font-weight:400;line-height:32px}
.product-sub{position:absolute;left:85px;top:2762px;width:360px;font-size:13px;line-height:21px;color:var(--text)}
.specs{position:absolute;left:85px;top:2826px;width:420px;list-style:none}
.specs li{position:relative;padding-left:20px;font-size:12.5px;line-height:25px;color:var(--text)}
.specs li::before{content:"";position:absolute;left:2px;top:10px;width:6px;height:6px;border-radius:50%;background:var(--ink)}
.product-rov{position:absolute;left:581px;top:2680px;width:281px;height:172px}
.price-label{position:absolute;left:553px;top:2916px;font-size:10px;color:var(--text)}
.price{position:absolute;left:553px;top:2930px;font-size:15px;font-weight:700}
.qty{position:absolute;left:640px;top:2914px;width:97px;height:32px;border:1px solid var(--line);background:#fff;display:flex;justify-content:space-around;align-items:center;font-size:12px}
.add-cart{position:absolute;left:754px;top:2914px;width:108px;height:32px;background:var(--accent);color:#fff;font-size:10.5px;font-weight:600;text-align:center;line-height:32px}

/* contact */
.contact-title{position:absolute;left:82px;top:3110px;font-size:26px;font-weight:500}
.contact-copy{position:absolute;left:82px;top:3163px;width:300px;font-size:11px;line-height:18px;color:var(--text)}
.office-title{position:absolute;left:82px;top:3280px;font-size:19px;font-weight:500;color:var(--accent)}
.office-copy{position:absolute;left:82px;top:3316px;width:230px;font-size:11px;line-height:18px;color:var(--text)}
.form-title{position:absolute;left:436px;top:3159px;font-size:16px;font-weight:500}
.field{position:absolute;width:202px;height:47px;border:1px solid #bdbdbd;border-radius:24px;padding-left:18px;font-size:12.5px;line-height:45px;color:var(--muted)}
.field.col2{left:660px}.field.col1{left:436px}
.field.message{left:436px;top:3418px;width:426px;height:96px;border-radius:8px;padding-top:14px;line-height:16px;padding-left:22px}
.send{position:absolute;left:436px;top:3537px;width:426px;height:48px;background:var(--accent);color:#fff;font-size:12px;font-weight:500;text-align:center;line-height:48px}

/* map */
.map{position:absolute;left:0;top:3636px;width:946px;height:277px;background:linear-gradient(120deg,#eef1ec 0%,#e4ebe3 40%,#cfe3f2 70%,#e8ede6 100%)}

/* footer */
.footer-brand{position:absolute;left:0;top:3992px;width:946px;display:flex;justify-content:center;align-items:center;gap:10px;font-size:15px;font-weight:700;color:var(--navy)}
.footer-dot{width:34px;height:34px;border-radius:50%;background:var(--deep)}
.footer-links{position:absolute;left:0;top:4097px;width:946px;display:flex;justify-content:center;gap:36px;font-size:12px}
.footer-rule{position:absolute;left:82px;top:4142px;width:780px;height:1px;background:var(--line)}
.copyright{position:absolute;left:0;top:4156px;width:946px;text-align:center;font-size:11px;color:var(--text)}
</style>
</head>
<body>
<main class="page">

  <header class="nav">
    <div class="brand"><span class="brand-dot"></span>BRINDLE GULL WATERS</div>
    <span class="nav-link active" style="left:500px">Home</span>
    <span class="nav-link" style="left:560px">About Us</span>
    <span class="nav-link" style="left:637px">How it works</span>
    <span class="nav-link" style="left:732px">Contact</span>
    <span class="nav-divider"></span>
    <svg class="abs" style="left:807px;top:16px" width="13" height="13" viewBox="0 0 13 13" fill="none" stroke="#555" stroke-width="1.3"><circle cx="5.5" cy="5.5" r="4"/><path d="M8.5 8.5L12 12"/></svg>
    <svg class="abs" style="left:833px;top:15px" width="15" height="15" viewBox="0 0 15 15" fill="none" stroke="#222" stroke-width="1.3"><path d="M1 2h2l2 8h7l2-6H4"/><circle cx="6" cy="13" r="1"/><circle cx="11" cy="13" r="1"/></svg>
    <span class="cart-badge">2</span>
  </header>

  <section>
    <div class="hero" role="img" aria-label="Scuba divers swimming in deep blue water"></div>
    <svg class="hero-curve" width="946" height="480" viewBox="0 0 946 480"><path d="M0 468 Q473 316 946 468 L946 480 L0 480 Z" fill="#fff"/></svg>
    <h1 class="hero-title">Text Of The Printing And<br>Typesetting Industry.</h1>
    <p class="hero-sub">Lorem Ipsum is simply dummy text</p>
    <a class="btn-white">Get a Price</a>
    <div class="hero-rov rov" role="img" aria-label="Underwater ROV drone with four thrusters"></div>
  </section>

  <section>
    <div class="photo-dive" role="img" aria-label="Divers exploring underwater"></div>
    <div class="photo-fish" role="img" aria-label="Lionfish in bright blue water"></div>
    <h2 class="h2 intro-title">Improved underwater control and dive into.</h2>
    <p class="intro-copy">Lorem ipsum dolor sit amet, consetetur sadipscing elitr, sed diam nonumy eirmod tempor invidunt ut labore et dolore magna aliquyam erat, sed diam voluptua. At vero eos et accusam et justo duo dolores et ea rebum. Stet clita kasd gubergren, no sea takimata sanctus est Lorem ipsum dolor sit amet. Lorem ipsum dolor sit amet, consetetur sadipscing elitr, sed diam nonumy eirmod tempor invidunt ut labore et dolore magna aliquyam erat, sed diam voluptua.</p>
    <a class="btn-accent" style="left:496px;top:1032px;width:134px">Get a Price</a>
  </section>

  <section>
    <div class="video-band" role="img" aria-label="Video still of a diver over a reef"></div>
    <h2 class="video-title">Underwater ROV</h2>
    <p class="video-copy">Lorem Ipsum is simply dummy text of the printing industry.</p>
    <svg class="play" width="60" height="60" viewBox="0 0 60 60"><circle cx="30" cy="30" r="29" fill="#ffffff" fill-opacity=".2"/><circle cx="30" cy="30" r="21" fill="#fff"/><path d="M26 22 L38 30 L26 38 Z" fill="#fa5a32"/></svg>
  </section>

  <section>
    <h2 class="lineup-title">View vehicle line-up</h2>
    <div class="tabs">
      <span class="tab" style="left:0">Underwater ROV</span>
      <span class="tab" style="left:147px">CCTV Pipe Crawlers</span>
      <span class="tab" style="left:314px">Utility Crawlers</span>
      <span class="tab" style="left:448px">Drop Camera</span>
    </div>
    <div class="tab-underline"></div>
    <div class="lineup-rov rov" role="img" aria-label="Underwater ROV drone"></div>
    <h3 class="lineup-name">Underwater ROV</h3>
    <p class="lineup-copy">Lorem ipsum dolor sit amet, consetetur sadipscing elitr, sed diam nonumy eirmod tempor invidunt ut labore et dolore magna aliquyam erat, sed diam voluptua. At vero eos et accusam et justo duo dolores et ea rebum. Stet clita kasd gubergren, no sea takimata sanctus est Lorem ipsum dolor sit</p>

    <h2 class="features-title">Features</h2>
    <div class="feature left" style="top:2145px">Drop camera</div>
    <div class="feature left" style="top:2184px">Underwater pipeline inspection</div>
    <div class="feature left" style="top:2223px">Electronics Charting &amp; GIS</div>
    <div class="feature left" style="top:2262px">Underwater hull inspection</div>
    <div class="feature left" style="top:2301px">Hydrographic Surveys</div>
    <div class="feature left" style="top:2340px">Aquarium</div>
    <div class="feature left" style="top:2379px">Marine Mapping &amp; Cartography</div>
    <div class="feature left" style="top:2418px">Boat Props</div>
    <div class="feature left" style="top:2457px">Pipeline Inspection, Construction</div>
    <div class="feature left last" style="top:2496px">ROV, AUV, USV</div>
    <div class="feature right" style="top:2145px">Dredging</div>
    <div class="feature right" style="top:2184px">Underwater, Weatherproof Security control system</div>
    <div class="feature right" style="top:2223px">Waterproof underwater inspection camera</div>
    <div class="feature right" style="top:2262px">General underwater inspection</div>
    <div class="feature right" style="top:2301px">Shallow sea culture construction inspection</div>
    <div class="feature right" style="top:2340px">Marine Environments</div>
    <div class="feature right" style="top:2379px">Boat bottom inspection</div>
    <div class="feature right" style="top:2418px">Offshore Construction</div>
    <div class="feature right" style="top:2457px">Port Harbar Surveying</div>
    <div class="feature right last" style="top:2496px">Steam Live Video</div>
  </section>

  <section>
    <div class="product"></div>
    <h2 class="product-title">Corrin DEEPFIN:<br>The Underwater ROV</h2>
    <p class="product-sub">Waterproof 3G-SDI monitor for KESTREL VISTA ORCA splash bag with combo</p>
    <ul class="specs">
      <li>Screen resolution 1920x1080, full HD resolution</li>
      <li>Input signal - SDI (for Kestrel Vista Mini,only 3G SDI cameras)</li>
      <li>The monitor is completely sealed and works above water</li>
      <li>Cooling fan inside, prevent overheating of the electronics</li>
      <li>No internal battery, power feed from an outside source (Vista, Orca cameras)</li>
    </ul>
    <div class="product-rov rov" role="img" aria-label="Corrin DEEPFIN underwater ROV"></div>
    <span class="price-label">Item Price</span>
    <span class="price">$1499.00</span>
    <div class="qty"><span>-</span><span>1</span><span>+</span></div>
    <a class="add-cart">ADD TO CART</a>
  </section>

  <section>
    <h2 class="contact-title">Contact us</h2>
    <p class="contact-copy">Please don't hesitate to contact us if you have any questions about our products, services, repairs, or other details about Brindle Gull Waters</p>
    <h3 class="office-title">Head Office</h3>
    <p class="office-copy">5 - Street dolor sit amet, consetetur sadipscing elitr, sed diam<br>Location - 888888</p>
    <h3 class="office-title" style="top:3396px">Support</h3>
    <p class="office-copy" style="top:3442px">support@brindlegullwaters.com</p>

    <h3 class="form-title">How can we help you?</h3>
    <div class="field col1" style="top:3208px">First Name</div>
    <div class="field col2" style="top:3208px">Last Name</div>
    <div class="field col1" style="top:3279px">Email ID</div>
    <div class="field col2" style="top:3279px">Contact Number</div>
    <div class="field col1" style="top:3349px">City
      <svg class="abs" style="left:168px;top:19px" width="11" height="8" viewBox="0 0 11 8" fill="none" stroke="#222" stroke-width="1.6"><path d="M1 1l4.5 5L10 1"/></svg>
    </div>
    <div class="field col2" style="top:3349px">mm/dd/yyyy</div>
    <div class="field message">Your Message</div>
    <a class="send">Send</a>
  </section>

  <div class="map" role="img" aria-label="Street map showing the office location by the river"></div>

  <footer>
    <div class="footer-brand"><span class="footer-dot"></span>BRINDLE GULL WATERS</div>
    <nav class="footer-links">
      <span>Home</span><span>About Us</span><span>How it works</span><span>Terms of Services</span><span>Privacy Policy</span><span>Contact Us</span>
    </nav>
    <div class="footer-rule"></div>
    <p class="copyright">Copyright © 2021 Brindle Gull Waters. All right has reserved.</p>
  </footer>

</main>
</body>
</html>
```